Wordpress Business Travel Blog and Discussion Board

Oh, Hello!

We are looking for a motivated designer to create a full, turnkey interactive WordPress website geared toward business travel that includes a news style blog (look at ByteHarbor.com and Wirevane.com for the style we like) that is seamlessly integrated with a robust message board (look at JetGabble.com and LoftCabin.com). Ok, so stick with us here because this is actually a pretty cool project that shouldn't be too hard, but yes, of course we have some curve balls that we are throwing your way. Sorry! :)

*On the front page*

- We would like to have a typical news style blog layout that is fun, somewhat professional, and easy to read. That's easy!

- Somewhere within first glance, we would like to have a short list of the most active discussions on our discussion board. (What's trending, or something like that). Not too bad, right?

- Overall, want to have a good amount of content, but we also do not want the visitor to feel as if he or she is having to sift through a lot of content to see what he or she wants to see. Great! We're past the beginning!

We will have traditional visual advertising on all of our pages. Please leave space as necessary :)

*On the Blog/News story pages*

Let's keep these simple - but there is a twist!

Let's say I create a blog/news post. I would like that blog/news post to also be opened as a discussion on the discussion board. For example, I write an article about Corvane Airways and their service on a particular international flight. This will be opened as a discussion under the Corvane Airways topic in the discussion board. Other users can also open new discussions under any topic on the discussion board, but they cannot post stories (unless permission is given) to the blog wall. We would like their posts to show up as regular discussion board posts while the news/blog posts by us show up as news/blog posts on the front page, *and* (oh yes we did!) as discussions in the discussion board. Of course, users will still be able to post comments to the news/blog post, which will also be posted in the discussion.

OK, does that make sense? Let me know if I can help make this more clear! :) Sorry!

*Wiki Pages*

Take a look at the Corvane Airways example above. In that example, my news/blog entry automatically opens a new discussion post. Although we won't necessarily need to create a new wiki page, we would like to tag the post and the discussion to a wiki page about the topic. The wiki page can be created and edited by all users (and locked by us if necessary). BONUS! Can we tag more than one wiki page?

*Websites that inspire us*

ByteHarbor.com - concept and design
Wirevane.com - concept and design
JetGabble.com - concept
LoftCabin.com - concept
pomwhisper.com - concept

All of the sites above are great and we can only thrive with their great success. We are not aiming to be a competitor to the travel sites, but just another great option for interested visitors. Please do not simply copy what they have. What is posted above is a list of our favorite sites that we visit every day.

Our favorite font is Segoe UI, but please don't use this (or a similar font) too much! Maybe just titles would be great. You're the designer so you can make the call here.

Also, our favorite color is blue, but if you have another favorite color, go ahead and show us what you can do! (Don't use too much blue!)

*Oh, and One More Thing*

(I know, you thought we were done. We're not!)

Here's the killer - We would like to create a way for people to, say, enter the details of their next trip and be matched with someone who will also be on a portion of their trip.

For example, let's say I am flying Brisola Airways flight 109 from Los Angeles to New York JFK Airport this Friday. I am staying at the Marrow Lodge Manhattan Central on Friday night, and I am flying back on Saturday night on Quessa flight 290 from New York JFK airport back to Los Angeles. Another user will also be on the Quessa flight back to Los Angeles with me and he entered that information in the website. (Note, the user has to manually enter this information). The other user and I will both be notified that there is at least one other user who will be on the same Quessa flight as me. We will both have the option to reveal our online identity - which will in fact be released to each person as long as each person *mutually* agrees.

This can be very simple - almost like a dating site type of match but it is based on two people being in the same place at the same time (based on what they report). Also, we would like to be able to collect this information - not necessarily tied to the user's true identity. The information we would like to have is - what the user is claiming he or she is doing on the trip (i.e. staying at the Marrow Lodge Central, flying Brisola Airways), and whether or not the user agreed to reveal his or her identity - AND! whether or not the users both revealed their identity.

*Most Important*

HAVE FUN and THANK YOU!! :)

A couple of quick notes - this is a design and code project. We are most likely offering a more $(!) design and code project for the version 2.0 of this website once we get user feedback from this first round.

Also, the name of the website is Veyrola. (www.veyrola.com)

Good luck!

• We need to have a high end, professional, modern, and clean design on the front page to entice readers to constantly visit and stay on our site.
• It would be great to give us the ability to automatically recognize users for visiting the website and/or participating and commenting. Social badges, recognition, etc. would be very cool.
• Although this is a website around business travel, we do not necessarily want it to be business travel themed. There can be hints of the theme, but otherwise the visual look should be somewhat generic.

```html
<!DOCTYPE html>
<html lang="en">
<head>
<meta charset="utf-8">
<title>Tarrow Travel</title>
<link rel="stylesheet" href="https://fonts.googleapis.com/css2?family=Roboto+Condensed:wght@300;400&family=Roboto:wght@400&display=swap">
<style>
:root{
  --blue:#1c6fc4;
  --nav-top:#3d95ea;
  --nav-bottom:#1f78d6;
  --link:#2a78cc;
  --text:#555;
  --dark:#333;
  --muted:#999;
  --rule:#c9c9c9;
  --green:#3aa617;
  --orange:#f39a1b;
  --footer:#333;
  --heading:"Roboto Condensed", sans-serif;
  --body:"Roboto", Arial, sans-serif;
}
*{margin:0;padding:0;box-sizing:border-box}
html,body{width:1024px;height:1200px;overflow:hidden;background:#fff}
body{position:relative;font-family:var(--body);color:var(--text);font-size:9.6px}
a{color:var(--link);text-decoration:none}
.abs{position:absolute}

/* header */
.brand{left:120px;top:20px;font-family:var(--heading);font-weight:400;font-size:31px;color:var(--blue);letter-spacing:.5px}
.search{left:745px;top:25px;width:158px;height:23px;border:2px solid #ddd;border-radius:12px;padding:0 7px;display:flex;align-items:center;justify-content:space-between;color:#666;font-size:9.6px}
.nav{left:0;top:74px;width:1024px;height:35px;background:linear-gradient(var(--nav-top),var(--nav-bottom))}
.nav ul{list-style:none;display:flex;position:absolute;left:113px;top:0;height:35px}
.nav li{height:35px;display:flex;align-items:center;padding:0 24px;color:#fff;font-family:var(--heading);font-size:13.5px;border-right:1px solid #1a67bb}
.nav li:last-child{border-right:0}

/* hero */
.slider{left:120px;top:122px;width:528px;height:189px;background:linear-gradient(120deg,#3b45a8,#6a78c8 45%,#2d3a8c);box-shadow:0 5px 5px -3px rgba(0,0,0,.3)}
.dots{right:8px;bottom:9px;display:flex;gap:5px}
.dots span{width:9px;height:9px;border-radius:50%;background:#ddd}
.ad-top{left:664px;top:122px;width:240px;height:199px;background:linear-gradient(135deg,#0d1a2a,#1a2c44 60%,#3a1010)}
.ad-side{left:664px;top:802px;width:240px;height:200px;background:linear-gradient(#f7a01e,#f07a10);border:1px solid #ddd}

/* trending */
.section-title{font-family:var(--heading);font-weight:300;font-size:15px;color:var(--dark)}
.post-title{font-family:var(--heading);font-weight:300;font-size:14px;color:var(--link)}
.meta{font-size:9.2px;color:var(--muted);margin-left:6px;font-family:var(--body)}
.post-img{width:160px;height:183px;background:linear-gradient(90deg,#1a1a1a,#6a3a22 35%,#1a1a1a 70%)}
.post-body{width:362px;line-height:16.8px;font-size:9.4px}
.post-body p+p{margin-top:12.8px}
.dotted{left:120px;width:528px;border-top:1px dotted #aaa}

/* lists */
.col-head{font-family:var(--heading);font-weight:300;font-size:15px;padding-bottom:4px}
.news .col-head{color:var(--green);border-bottom:3px solid var(--green)}
.reviews .col-head{color:var(--orange);border-bottom:3px solid var(--orange)}
.news-item{position:absolute;left:0;line-height:15.5px}
.news-item h4{font-weight:400;font-size:10.8px;color:var(--dark)}
.news-item .cat{color:#777;font-size:9.6px}
.review{position:absolute;left:0;display:flex;gap:6px;line-height:14.4px}
.review .thumb{width:60px;height:44px;background:linear-gradient(90deg,#2a1a10,#8a5a30 50%,#2a1a10);flex:none;margin-top:-2px}
.review p{width:186px;font-size:9.6px;color:#666}
.review small{display:block;color:#aaa;font-size:9.6px;margin-top:2px}

/* blogs box */
.blogs{left:664px;top:342px;width:240px;height:446px;border:1px solid #d5d5d5}
.blogs-head{position:absolute;left:9px;top:7px;width:186px;display:flex;align-items:center;gap:5px;font-family:var(--heading);font-size:13.5px;color:var(--blue);border-bottom:1px solid #aaa;padding-bottom:2px}
.blogs-head i{width:11px;height:11px;background:var(--orange);display:flex;align-items:center;justify-content:center}
.entry{position:absolute;left:9px;width:224px}
.entry .date{font-family:var(--heading);font-size:9.6px;color:var(--dark)}
.entry .row{display:flex;gap:11px;margin-top:4px}
.entry .avatar{width:39px;height:39px;background:linear-gradient(#8a8a8a,#c9a08a);flex:none;margin-top:2px}
.entry .txt{line-height:16px;font-size:9.4px}
.more{right:7px;bottom:9px;font-size:9.6px}

/* footer */
.footer{left:0;top:1128px;width:1024px;height:43px;background:var(--footer);color:#fff;font-size:9.6px}
.footer .links{position:absolute;top:16px}
.footer .sep{margin:0 7px}
.follow{position:absolute;left:690px;top:12px;font-family:var(--heading);font-size:13.5px}
.social{position:absolute;left:771px;top:8px;display:flex;gap:10px}
.social span{width:26px;height:26px;border-radius:50%}
.copy{left:120px;top:1180px;font-size:9.6px;color:var(--dark)}
</style>
</head>
<body>

<header>
  <div class="abs brand">TARROW TRAVEL</div>
  <div class="abs search">Search
    <svg width="14" height="14" viewBox="0 0 14 14"><circle cx="5.5" cy="5.5" r="4" fill="none" stroke="#555" stroke-width="1.6"/><line x1="8.5" y1="8.5" x2="12.5" y2="12.5" stroke="#555" stroke-width="2"/></svg>
  </div>
  <nav class="abs nav"><ul><li>Home</li><li>News</li><li>Whats trending</li><li>Blog</li><li>Contact us</li></ul></nav>
</header>

<div class="abs slider" role="img" aria-label="Photo of award winners holding framed certificates on stage">
  <div class="abs dots"><span></span><span></span><span></span></div>
</div>
<div class="abs ad-top" role="img" aria-label="Advertisement banner for a mobility forum event"></div>

<section>
  <h2 class="abs section-title" style="left:121px;top:350px">Whats Trending</h2>

  <h3 class="abs post-title" style="left:120px;top:373px">Hands-On With The New Lumo Phone 5<span class="meta">2 days ago, by veltstyle</span></h3>
  <div class="abs post-img" style="left:120px;top:400px" role="img" aria-label="Hand holding a smartphone"></div>
  <div class="abs post-body" style="left:287px;top:395px">
    <p>Lorem Ipsum is simply dummy text of the printing and typesetting industry. Lorem Ipsum has been the industry's standard dummy text ever since the 1500s, when an unknown printer took a galley of type and scrambled it to make a type specimen book. It has survived not only five centuries, but also the leap into electronic typesetting, remaining essentially unchanged.</p>
    <p>It was popularised in the 1960s with the release of Latterset sheets containing Lorem Ipsum passages, and more recently with desktop publishing software like Alder PageForge including versions of Lorem Ipsum.</p>
  </div>
  <div class="abs dotted" style="top:596px"></div>

  <h3 class="abs post-title" style="left:120px;top:615px">Hands-On With The New Lumo Phone 5<span class="meta">2 days ago, by veltstyle</span></h3>
  <div class="abs post-img" style="left:120px;top:642px" role="img" aria-label="Hand holding a smartphone"></div>
  <div class="abs post-body" style="left:287px;top:637px">
    <p>Lorem Ipsum is simply dummy text of the printing and typesetting industry. Lorem Ipsum has been the industry's standard dummy text ever since the 1500s, when an unknown printer took a galley of type and scrambled it to make a type specimen book. It has survived not only five centuries, but also the leap into electronic typesetting, remaining essentially unchanged.</p>
    <p>It was popularised in the 1960s with the release of Latterset sheets containing Lorem Ipsum passages, and more recently with desktop publishing software like Alder PageForge including versions of Lorem Ipsum.</p>
  </div>
  <div class="abs dotted" style="top:838px"></div>
</section>

<section class="abs news" style="left:120px;top:864px;width:252px;height:220px">
  <h2 class="col-head">News</h2>
  <div class="news-item" style="top:41px"><h4>Harbor City Style Week Coverage: Day 4</h4><div class="cat">Fashion &amp; Trends | 2 days ago, by veltstyle</div><a href="#">Read More...</a></div>
  <div class="news-item" style="top:101px"><h4>Harbor City Style Week Coverage: Day 4</h4><div class="cat">Fashion &amp; Trends | 2 days ago, by veltstyle</div><a href="#">Read More...</a></div>
  <div class="news-item" style="top:166px"><h4>Harbor City Style Week Coverage: Day 4</h4><div class="cat">Fashion &amp; Trends | 2 days ago, by veltstyle</div><a href="#">Read More...</a></div>
</section>

<section class="abs reviews" style="left:397px;top:864px;width:252px;height:255px">
  <h2 class="col-head">Recent Reviews</h2>
  <div class="review" style="top:34px"><div class="thumb" role="img" aria-label="Electric longboard"></div><p>Drift Board electric longboard is light-weight enough to carry, powerful enough to haul riders uphill<small>4 hours ago</small></p></div>
  <div class="review" style="top:104px"><div class="thumb" role="img" aria-label="Electric longboard"></div><p>Drift Board electric longboard is light-weight enough to carry, powerful enough to haul riders uphill<small>4 hours ago</small></p></div>
  <div class="review" style="top:175px"><div class="thumb" role="img" aria-label="Electric longboard"></div><p>Drift Board electric longboard is light-weight enough to carry, powerful enough to haul riders uphill<small>4 hours ago</small></p></div>
  <a href="#" style="position:absolute;right:2px;top:239px">See All...</a>
</section>

<aside class="abs blogs">
  <div class="blogs-head"><i><svg width="7" height="7" viewBox="0 0 7 7"><path d="M1 0L6 3.5L1 7Z" fill="#fff"/></svg></i>From the Blogs</div>
  <div class="entry" style="top:33px"><div class="date">September11,2012</div><div class="row"><div class="avatar" role="img" aria-label="Author portrait"></div><div class="txt"><a href="#">Lorem Ipsum is simply dummy text of the</a><br>Lorem Ipsum is simply dummy text of the printing and typesetting industry.<br><a href="#">Read more...</a></div></div></div>
  <div class="entry" style="top:132px"><div class="date">September11,2012</div><div class="row"><div class="avatar" role="img" aria-label="Author portrait"></div><div class="txt"><a href="#">Lorem Ipsum is simply dummy text of the</a><br>Lorem Ipsum is simply dummy text of the printing and typesetting industry.<br><a href="#">Read more...</a></div></div></div>
  <div class="entry" style="top:235px"><div class="date">September11,2012</div><div class="row"><div class="avatar" role="img" aria-label="Author portrait"></div><div class="txt"><a href="#">Lorem Ipsum is simply dummy text of the</a><br>Lorem Ipsum is simply dummy text of the printing and typesetting industry.<br><a href="#">Read more...</a></div></div></div>
  <div class="entry" style="top:338px"><div class="date">September11,2012</div><div class="row"><div class="avatar" role="img" aria-label="Author portrait"></div><div class="txt"><a href="#">Lorem Ipsum is simply dummy text of the</a><br>Lorem Ipsum is simply dummy text of the printing and typesetting industry.<br><a href="#">Read more...</a></div></div></div>
  <a class="abs more" href="#"><span style="color:#555">&rarr;</span> More From the Blogs</a>
</aside>

<div class="abs ad-side" role="img" aria-label="Advertisement banner for a domain and website service"></div>

<footer class="abs footer">
  <div class="links" style="left:120px">Home<span class="sep">/</span>About us<span class="sep">/</span>Contact</div>
  <div class="links" style="left:458px">Privacy<span class="sep">/</span>Terms of Use</div>
  <div class="follow">Follow us on</div>
  <div class="social">
    <span style="background:#3b5a9a"></span>
    <span style="background:#2ea9e0"></span>
    <span style="background:#e6e6e6"></span>
    <span style="background:#f39219"></span>
  </div>
</footer>
<div class="abs copy">&copy; 2012 Tarrow Travel. All rights reserved.</div>

</body>
</html>
```